Deactivated Coal-Fired Power Plant to be redeveloped into a Green Energy Campus.

Want a striking business card statement that introduces our concept project to provide economic and community recovery to a former rural coal community in western PA.
Essentially 12 project representatives that will lead both the demolition of an existing power plant and the redevelopment to a new Green energy site.
Business Card should reflect our effort.
We are open to ideas.

Target Market(s)

Energy and Power Generation industries

Industry/Entity Type

Power Generation and Data Centers

Contact Information for Business Card

Included in uploaded materials

Font styles to use
Sans Serif
Other font styles liked:
• Arial, Calibri

Requirements
Must have
• Multiple colors

```html
<!DOCTYPE html>
<html lang="en">
<head>
<meta charset="utf-8">
<title>Ridgeview Redevelopment – Business Card</title>
<link rel="stylesheet" href="https://fonts.googleapis.com/css2?family=Montserrat:wght@500;700&family=Open+Sans:wght@400&display=swap">
<style>
  :root {
    --backdrop: #2a2a2a;
    --card-white: #ffffff;
    --brand-green: #1e9a48;
    --deep-green: #1d5a26;
    --ink: #1a1a1a;
    --muted-ink: #3a3a3a;
  }
  * { box-sizing: border-box; margin: 0; padding: 0; }
  html, body { width: 1200px; height: 689px; overflow: hidden; }
  body {
    background: var(--backdrop);
    position: relative;
    font-family: "Open Sans", Arial, sans-serif;
  }
  .card {
    position: absolute;
    top: 190px;
    width: 540px;
    height: 309px;
    border-radius: 18px;
    overflow: hidden;
  }
  .card--front { left: 40px; }
  .card--back { left: 620px; background: var(--card-white); }

  .site-photo {
    position: absolute; inset: 0;
    background: linear-gradient(160deg, #8fa3a8 0%, #6f8a66 28%, #4d6b3e 55%, #3d5a33 75%, var(--deep-green) 100%);
  }
  .site-photo::after {
    content: ""; position: absolute; left: 0; right: 0; bottom: 0; height: 45%;
    background: linear-gradient(to bottom, rgba(29,90,38,0) 0%, rgba(29,110,45,0.9) 100%);
  }
  .statement {
    position: absolute; left: 28px; right: 24px; bottom: 34px;
    font-family: "Montserrat", Arial, sans-serif;
    font-weight: 700;
    font-size: 16px;
    line-height: 1.35;
    color: var(--card-white);
    text-transform: uppercase;
  }

  .brand {
    position: absolute; left: 30px; top: 128px;
    display: flex; align-items: center; gap: 10px;
    width: 190px;
  }
  .brand__dot {
    flex: none;
    width: 34px; height: 34px; border-radius: 50%;
    background: var(--brand-green);
  }
  .brand__name {
    font-family: "Montserrat", Arial, sans-serif;
    font-weight: 700; font-size: 14px; line-height: 1.2;
    color: var(--ink); text-transform: uppercase;
  }
  .contact {
    position: absolute; left: 248px; top: 62px; right: 18px;
  }
  .contact__name {
    font-family: "Montserrat", Arial, sans-serif;
    font-weight: 700; font-size: 22px;
    color: var(--brand-green); text-transform: uppercase;
    letter-spacing: 0.3px;
  }
  .contact__title {
    font-size: 14px; color: var(--muted-ink); margin-top: 2px;
  }
  .contact__rule {
    width: 44px; height: 2px; background: var(--brand-green);
    margin: 18px 0 16px;
  }
  .contact__line {
    display: flex; align-items: center; gap: 8px;
    font-size: 13px; color: var(--ink); margin-bottom: 6px;
    white-space: nowrap;
  }
  .contact__line svg { flex: none; }
</style>
</head>
<body>
  <section class="card card--front">
    <div class="site-photo" role="img" aria-label="Aerial photograph of a coal-fired power plant with tall smokestacks in green rolling hills"></div>
    <p class="statement">Deactivated coal-fired power plant to be<br>redeveloped into a green energy campus</p>
  </section>

  <section class="card card--back">
    <div class="brand">
      <span class="brand__dot"></span>
      <span class="brand__name">Ridgeview<br>Redevelopment</span>
    </div>
    <div class="contact">
      <h1 class="contact__name">Daniel Whitford</h1>
      <p class="contact__title">Chief Redevelopment LLC</p>
      <div class="contact__rule"></div>
      <p class="contact__line">
        <svg width="13" height="13" viewBox="0 0 24 24" aria-hidden="true"><path fill="var(--brand-green)" d="M6.6 10.8a15.1 15.1 0 0 0 6.6 6.6l2.2-2.2a1 1 0 0 1 1-.25 11.4 11.4 0 0 0 3.6.57 1 1 0 0 1 1 1V20a1 1 0 0 1-1 1A17 17 0 0 1 3 4a1 1 0 0 1 1-1h3.5a1 1 0 0 1 1 1c0 1.250.2 2.45.57 3.6a1 1 0 0 1-.25 1z"/></svg>
        555.014.2290
      </p>
      <p class="contact__line">
        <svg width="13" height="13" viewBox="0 0 24 24" aria-hidden="true"><path fill="var(--brand-green)" d="M2 5h20v14H2z"/><path fill="none" stroke="#fff" stroke-width="1.8" d="M2.5 5.5 12 13l9.5-7.5"/></svg>
        dwhitford@ridgeviewredevelopment.com
      </p>
    </div>
  </section>
</body>
</html>
```